Band and Coaching business card (creative industry)

My company The Birch Ensemble is the name of my band Soul outfit but is also a brand I use for my coaching business which is Performance coaching in the following areas: Corporate coaching, acting, vocals and dialect. The band plays for corporate events and private functions as well as local bar/restaurant/festivals.

Hi All

Please see updated info for the wording of the business card front and back.  This is ito then be followed with contact number, email and facebook link

first side should have:

Rosalind Pettigrew
Creative Director
( followed by contact info as per previous)

Side 2:

The Birch Ensemble  - Band  
 Vocalist      I   Musician    I  Songwriter

The Birch Ensemble  - Studio
Performance Coaching  
Acting  I  Vocals  I Dialect  I Corporate Coaching

Industry/Entity Type

Events

Contact Information for Business Card

The Birch Ensemble (logo)
Rosalind Pettigrew
Musician/Vocalist/Performance Coach
M: 0412 655 918
E: thebirchensemble@mailpost.example
W: www.socialpage.example/thebirchensembleband

Font styles to use
Sans Serif

Requirements
Must have
• first side should have:

Rosalind Pettigrew
Creative Director

Side 2:

The Birch Ensemble - Band
Vocalist I Musician I Songwriter

The Birch Ensemble - Studio
Performance Coaching
Acting I Vocals I Dialect I Corporate Coaching
Nice to have
• I like smaller business cards with curved edges.

some ideas for look in additional business cards attached.
Should not have
• music notes or anything specific to the field. Want to keep it funky and contemporary

```html
<!DOCTYPE html>
<html lang="en">
<head>
<meta charset="utf-8">
<title>The Birch Ensemble – Business Card</title>
<link rel="stylesheet" href="https://fonts.googleapis.com/css2?family=Ubuntu:wght@400;500;700&display=swap">
<style>
  :root {
    --page-bg: #f1f1f1;
    --card-navy: #1f2535;
    --card-navy-light: #2c3447;
    --text-light: #e4e8ef;
    --text-muted: #b9c0cc;
    --strip-light: #dfe4ed;
    --strip-text: #1f2535;
    --divider: #5b6477;
  }
  * { box-sizing: border-box; margin: 0; padding: 0; }
  html, body {
    width: 960px; height: 1200px; overflow: hidden;
    background: var(--page-bg);
    font-family: "Ubuntu", sans-serif;
  }
  .canvas { position: relative; width: 960px; height: 1200px; }

  .card {
    position: absolute; left: 100px;
    width: 760px; height: 416px;
    background: var(--card-navy);
    border-radius: 20px;
    overflow: hidden;
    box-shadow: 0 6px 18px rgba(0,0,0,0.18);
  }
  .card--front { top: 144px; }
  .card--back { top: 640px; }

  .card__texture {
    position: absolute; top: 0; width: 230px; height: 110px;
  }
  .card--front .card__texture {
    right: 0;
    background: radial-gradient(ellipse at 70% 10%, rgba(80,92,118,0.45), rgba(31,37,53,0) 70%);
  }
  .card--back .card__texture {
    left: 0;
    background: radial-gradient(ellipse at 25% 10%, rgba(80,92,118,0.45), rgba(31,37,53,0) 70%);
  }

  /* Front */
  .identity {
    position: absolute; left: 84px; top: 160px;
    display: flex; align-items: center; height: 88px;
  }
  .identity__name {
    width: 388px;
    font-weight: 700; font-size: 28px; color: var(--text-light);
    white-space: nowrap;
  }
  .identity__divider {
    width: 2px; height: 88px; background: var(--divider);
  }
  .identity__role {
    margin-left: 32px;
    font-size: 24px; color: var(--text-light);
    white-space: nowrap;
  }

  .contact-tab {
    position: absolute; left: 86px; bottom: 0;
    width: 630px; height: 70px;
  }
  .contact-tab__shape { position: absolute; left: 0; top: 0; }
  .contact-tab__content {
    position: relative; height: 100%;
    display: flex; align-items: center; justify-content: center;
    gap: 10px; padding-top: 4px;
    font-size: 19px; color: var(--strip-text);
    white-space: nowrap;
  }
  .contact-tab__icon {
    position: relative;
    flex: 0 0 32px;
    width: 32px; height: 32px; border-radius: 50%;
    background: var(--card-navy);
    display: flex; align-items: center; justify-content: center;
  }
  .contact-tab__icon svg { display: block; }
  .contact-tab__email { margin-right: 4px; }
  .contact-tab__phone { margin-left: 2px; }

  /* Back */
  .ensemble-title {
    position: absolute; left: 0; right: 0; top: 82px;
    text-align: center;
    font-weight: 500; font-size: 40px; color: var(--text-light);
  }
  .services {
    position: absolute; left: 12px; right: 12px; top: 188px; height: 82px;
    display: flex; align-items: center; gap: 3px;
  }
  .services__label {
    flex: 0 0 26px;
    width: 26px; height: 82px;
    background: var(--strip-light);
    display: flex; align-items: center; justify-content: center;
  }
  .services__label span {
    transform: rotate(-90deg);
    font-weight: 700; font-size: 15px; letter-spacing: 1px;
    color: var(--strip-text); white-space: nowrap;
  }
  .services__label--studio span { transform: rotate(90deg); }
  .services__group { display: flex; gap: 3px; }
  .services__group--band { transform: translateY(-5px); }
  .services__group--studio { transform: translateY(5px); flex: 1; }
  .services__item {
    height: 64px; padding: 0 11px;
    background: var(--strip-light);
    display: flex; align-items: center; justify-content: center;
    font-size: 17px; color: var(--strip-text); white-space: nowrap;
  }
  .services__group--studio .services__item { flex: 1 1 auto; }

  .social-link {
    position: absolute; left: 0; right: 0; top: 328px;
    text-align: center;
    font-size: 21px; color: var(--text-muted);
  }
</style>
</head>
<body>
<main class="canvas">

  <section class="card card--front" aria-label="Business card front">
    <div class="card__texture" role="img" aria-label="Faint scattered square texture"></div>
    <div class="identity">
      <h1 class="identity__name">Rosalind Pettigrew</h1>
      <div class="identity__divider"></div>
      <p class="identity__role">Creative Director</p>
    </div>
    <div class="contact-tab">
      <svg class="contact-tab__shape" width="630" height="70" viewBox="0 0 630 70" aria-hidden="true">
        <path d="M0,70 Q16,70 16,54 L16,18 Q16,0 34,0 L596,0 Q614,0 614,18 L614,54 Q614,70 630,70 Z" fill="#dfe4ed"/>
      </svg>
      <div class="contact-tab__content">
        <span class="contact-tab__email">thebirchensemble@mailpost.example</span>
        <span class="contact-tab__icon" aria-label="Email">
          <svg width="18" height="14" viewBox="0 0 18 14"><rect x="1" y="1" width="16" height="12" rx="1.5" fill="none" stroke="#e4e8ef" stroke-width="2"/><path d="M1.5,2 L9,8 L16.5,2" fill="none" stroke="#e4e8ef" stroke-width="2"/></svg>
        </span>
        <span class="contact-tab__icon" aria-label="Phone">
          <svg width="16" height="16" viewBox="0 0 16 16"><rect x="1" y="10" width="3" height="5" fill="#e4e8ef"/><rect x="6" y="6" width="3" height="9" fill="#e4e8ef"/><rect x="11" y="2" width="3" height="13" fill="#e4e8ef"/></svg>
        </span>
        <span class="contact-tab__phone">0412 655 918</span>
      </div>
    </div>
  </section>

  <section class="card card--back" aria-label="Business card back">
    <div class="card__texture" role="img" aria-label="Faint scattered square texture"></div>
    <h2 class="ensemble-title">The Birch Ensemble</h2>
    <div class="services">
      <div class="services__label"><span>BRAND</span></div>
      <div class="services__group services__group--band">
        <span class="services__item">Vocalist</span>
        <span class="services__item">Musician</span>
        <span class="services__item">Songwriter</span>
      </div>
      <div class="services__group services__group--studio">
        <span class="services__item">Acting</span>
        <span class="services__item">Vocals</span>
        <span class="services__item">Dialect</span>
        <span class="services__item">Corporate Coaching</span>
      </div>
      <div class="services__label services__label--studio"><span>STUDIO</span></div>
    </div>
    <p class="social-link">www.socialpage.example/thebirchensembleband</p>
  </section>

</main>
</body>
</html>
```